Design Project - Finance Website (Only need PSD)

UPDATED PROJECT (Now only PSD needed)
Need a Wordpress design for a company called "Tavernor Brook Finance". The company provides finance for corporate clients, businesses and property developers. The design should be business like with appealing colours that communicate trust. I have uploaded a banner and logo to be incorporated or feel free to design something better if you think you can.
** I now only need the PSD
** I want something that is actually designed rather than from a template.
Thanks
Updates
The website will be used for lead generation so the contact form with adjustable fields in the Wordpress backend should be fairly prominent on the page.
I have uploaded a banner and logo for the site. None of the designs I have seen so far were good enough so the first decent design using the new banner and logo provided will win the job. I do not want just a template that has been cut and paste from somewhere else, I want decent design. If anyone provides a decent design then I will give an extra bonus of $150.
Reason: I have uploaded a banner and logo for the site. None of the designs I have seen so far were good enough so the first decent design using the new banner and logo provided will win the job. I do not want just a template that has been cut and paste from somewhere else, I want decent design. If anyone provides a decent design then I will give an extra bonus of $150.
Thanks
Target Market(s)
Business owners & property developers
Industry/Entity Type
Finance
Requirements
Must have
- Contact form on home page that can be altered through the back end eg. ability to add or remove fields. Widgetised sidebars.
Nice to have
- Widgetised footer.

```html
<!DOCTYPE html>
<html lang="en">
<head>
<meta charset="utf-8">
<title>Tavernor Brook Finance</title>
<link rel="stylesheet" href="https://fonts.googleapis.com/css2?family=Arimo:wght@400;700&family=Didact+Gothic&family=Open+Sans:wght@400;600&display=swap">
<style>
:root{
  --page:#efefef;
  --ink:#111;
  --text:#555;
  --muted:#777;
  --blue:#4db8ec;
  --blue-deep:#2e8fc6;
  --blue-tab:#6bb8e8;
  --banner:#161616;
  --panel:#f7f7f7;
  --border:#d4d4d4;
  --footer:#a9d3f2;
  --footer-top:#dcdcdc;
}
*{box-sizing:border-box;margin:0;padding:0}
html,body{width:1033px;height:1200px;overflow:hidden}
body{background:var(--page);font-family:"Arimo",Arial,sans-serif;color:var(--text);position:relative}
.abs{position:absolute}

.search{left:676px;top:19px;width:192px;height:26px;background:linear-gradient(#e4e4e4,#f3f3f3);border-top:2px solid #d0d0d0;font-size:12px;color:#888;padding:5px 8px}
.search svg{position:absolute;right:6px;top:3px}
.social{top:19px;width:26px;height:26px;border-radius:50%;background:radial-gradient(circle at 40% 35%,#8a8a8a,#333)}

.brand{left:63px;top:55px;font-size:21px;color:var(--blue)}
.header-rule{left:312px;top:68px;width:645px;height:2px;background:#dcdcdc;border-bottom:1px solid #fff}

.nav{right:73px;top:93px;display:flex;gap:26px;font-family:"Didact Gothic",sans-serif;font-size:18px;color:#666}
.nav .active{color:var(--blue-deep);border-bottom:2px solid var(--blue);padding-bottom:2px}

.banner{left:63px;top:137px;width:901px;height:350px;background:linear-gradient(#1d1d1d,#0e0e0e)}
.banner-frame{left:20px;top:19px;width:457px;height:311px;background:#c9c9c9;border-radius:6px;padding:8px}
.banner-photo{width:100%;height:100%;background:linear-gradient(135deg,#7ea3c8 0%,#d7e9ef 45%,#a6cbd7 100%)}
.banner-device{left:403px;top:165px;width:94px;height:170px;background:linear-gradient(#f4f4f4,#d8d8d8);border:3px solid #2a2a2a}
.banner-lines{left:522px;top:115px;font-family:"Didact Gothic",sans-serif;font-size:21px;line-height:1}
.banner-lines p{position:absolute;left:0;white-space:nowrap}
.stars{left:797px;top:300px;display:flex;gap:6px}

.welcome{left:77px;top:487px;width:878px;height:202px;background:var(--panel);border:1px solid #e4e4e4;border-top:none}
.welcome h1{position:absolute;left:27px;top:20px;font-family:"Didact Gothic",sans-serif;font-weight:400;font-size:22px;color:var(--ink)}
.welcome h1 span{color:var(--blue-deep)}
.welcome p{position:absolute;left:29px;top:66px;width:820px;font-size:11.5px;line-height:16px;color:#666}
.btn-pill{left:723px;top:158px;width:124px;height:26px;border-radius:13px;background:linear-gradient(#9fd3f4,#3f93c9);border:1px solid #2f6f99;color:#fff;font-size:15px;text-align:center;line-height:24px}
.divider{left:100px;top:692px;width:832px;height:1px;background:#d0d0d0}
.divider-badge{left:492px;top:656px;width:66px;height:66px;border-radius:50%;background:var(--page)}

.col{top:765px;width:287px;height:276px;background:var(--panel);border:2px solid var(--border)}
.tab{top:738px;width:212px;height:33px;background:linear-gradient(#8ccbf2,#5aa9e0);color:#fff;font-family:"Open Sans",sans-serif;font-size:15px;display:flex;align-items:center;padding-left:32px;gap:10px;letter-spacing:.5px}
.tab b{width:21px;height:21px;border-radius:50%;border:2px solid #fff;font-weight:400;font-size:12px;display:flex;align-items:center;justify-content:center;margin-left:-20px}
.small{font-size:10.5px;line-height:14.5px;color:#333;text-align:justify}
.btn-sq{width:78px;height:18px;background:var(--blue);color:#fff;font-size:10.5px;text-align:center;line-height:18px}
.icon-fill{border-radius:3px}

.label{font-size:11.5px;color:#666;text-align:right;width:60px}
.field{left:731px;width:206px;height:30px;background:#fff;border:1px solid #dedede;border-radius:3px}
.check{left:731px;top:946px;width:13px;height:13px;border:1px solid #999;background:#fff}
.check-label{left:751px;top:944px;font-size:13px;color:#777}
.submit{left:826px;top:980px;width:105px;height:33px;border-radius:4px;background:linear-gradient(#7a7a7a,#1c1c1c 55%,#333);border:1px solid #000;color:#fff;font-family:"Open Sans",sans-serif;font-size:16px;text-align:center;line-height:30px;font-style:italic}

.footer-top{left:0;top:1067px;width:1033px;height:16px;background:var(--footer-top)}
.footer{left:0;top:1083px;width:1033px;height:117px;background:repeating-linear-gradient(135deg,var(--footer) 0 3px,#b3d9f5 3px 6px)}
.footer-links{top:1105px;list-style:none;font-size:10.5px;line-height:16.2px;color:#fff}
.footer-brand{left:720px;top:1104px;font-size:20px;color:#fff}
.copyright{left:851px;top:1156px;font-size:10.5px;color:#fff}
</style>
</head>
<body>

<div class="abs search">Search
  <svg width="24" height="20" viewBox="0 0 24 20"><circle cx="9" cy="8" r="6" fill="none" stroke="#3aa6e0" stroke-width="2.5"/><line x1="13" y1="12" x2="20" y2="18" stroke="#3aa6e0" stroke-width="3" stroke-linecap="round"/></svg>
</div>
<div class="abs social" style="left:900px"></div>
<div class="abs social" style="left:939px"></div>

<div class="abs brand">Tavernor Brook Finance</div>
<div class="abs header-rule"></div>

<nav class="abs nav">
  <span class="active">Home</span><span>About Us</span><span>Services</span><span>Finance</span><span>Real Estate</span><span>Contact Us</span>
</nav>

<section class="abs banner">
  <div class="abs banner-frame"><div class="banner-photo" role="img" aria-label="Photo of a pen resting on a printed stock chart"></div></div>
  <div class="abs banner-device" role="img" aria-label="Printed brochure showing the website layout"></div>
  <div class="abs banner-lines">
    <p style="top:12px;color:#ddd">Compare several capital provider rates</p>
    <p style="top:58px;color:#fff">Access to real estate and hedge funds</p>
    <p style="top:99px;color:var(--blue)">Optimise your capital returns</p>
  </div>
  <div class="abs stars">
    <svg width="24" height="24" viewBox="0 0 24 24"><polygon points="12,1 15,9 23,9 17,14 19,22 12,17 5,22 7,14 1,9 9,9" fill="#4db8ec"/></svg>
    <svg width="24" height="24" viewBox="0 0 24 24"><polygon points="12,1 15,9 23,9 17,14 19,22 12,17 5,22 7,14 1,9 9,9" fill="#4db8ec"/></svg>
    <svg width="24" height="24" viewBox="0 0 24 24"><polygon points="12,1 15,9 23,9 17,14 19,22 12,17 5,22 7,14 1,9 9,9" fill="none" stroke="#ddd" stroke-width="1.5"/></svg>
  </div>
</section>

<section class="abs welcome">
  <h1>Welcome to <span>TAVERNOR BROOK FINANCE</span></h1>
  <p>Lorem ipsum dolor sit amet, consectetur adipisicing elit, sed do eiusmod tempor incididunt ut labore et dolore magna aliqua. Ut enim ad minim veniam, quis nostrud exercitation ullamco laboris nisi ut aliquip ex ea commodo consequat. Duis aute irure dolor in reprehenderit in voluptate velit esse cillum dolore eu fugiat nulla pariatur. Excepteur sint occaecat cupidatat non proident, sunt in culpa qui officia deserunt mollit anim id est laborum. Lorem ipsum dolor sit amet, consectetur adipisicing elit, sed do eiusmod tempor incididunt ut labore et dolore magna aliqua. Ut enim ad minim veniam, quis nostrud exercitation ullamco laboris nisi ut aliquip ex ea commodo consequat. Duis aute irure dolor in reprehenderit in voluptate velit esse cillum dolore eu fugiat nulla pariatur. Excepteur sint occaecat cupidatat non proident, sunt in culpa qui officia deserunt mollit anim id est laborum.</p>
  <div class="abs btn-pill">Read More</div>
</section>
<div class="abs divider"></div>
<div class="abs divider-badge">
  <svg width="66" height="66" viewBox="0 0 66 66"><rect x="17" y="34" width="9" height="13" fill="#e8b23a"/><rect x="27" y="27" width="9" height="20" fill="#6bbf4a"/><rect x="37" y="20" width="9" height="27" fill="#e0453a"/></svg>
</div>

<!-- Latest news -->
<div class="abs tab" style="left:109px"><b>1</b>Latest News....</div>
<section class="abs col" style="left:74px">
  <div class="abs icon-fill" style="left:13px;top:23px;width:48px;height:64px;background:linear-gradient(#b9dcf3,#3d7cb8)" role="img" aria-label="Information booklet icon"></div>
  <p class="abs small" style="left:77px;top:32px;width:197px">Lorem ipsum dolor sit amet, consectetur adipisicing elit, sed do eiusmod tempor incididunt ut labore et dolore magna aliqua.</p>
  <div class="abs btn-sq" style="left:196px;top:76px">Read more</div>
  <div class="abs icon-fill" style="left:13px;top:106px;width:48px;height:64px;background:linear-gradient(#b9dcf3,#3d7cb8)" role="img" aria-label="Information booklet icon"></div>
  <p class="abs small" style="left:77px;top:115px;width:197px">Lorem ipsum dolor sit amet, consectetur adipisicing elit, sed do eiusmod tempor incididunt ut labore et dolore magna aliqua.</p>
  <div class="abs btn-sq" style="left:196px;top:159px">Read more</div>
  <div class="abs icon-fill" style="left:13px;top:189px;width:48px;height:64px;background:linear-gradient(#b9dcf3,#3d7cb8)" role="img" aria-label="Information booklet icon"></div>
  <p class="abs small" style="left:77px;top:200px;width:197px">Lorem ipsum dolor sit amet, consectetur adipisicing elit, sed do eiusmod tempor incididunt ut labore et dolore magna aliqua.</p>
  <div class="abs btn-sq" style="left:196px;top:243px">Read more</div>
</section>

<!-- Case study -->
<div class="abs tab" style="left:409px"><b>2</b>Case Study....</div>
<section class="abs col" style="left:373px">
  <div class="abs icon-fill" style="left:10px;top:30px;width:86px;height:72px;background:linear-gradient(135deg,#efe6f3,#c7b2d6 60%,#e49a4a)" role="img" aria-label="Notepad and pencil illustration"></div>
  <p class="abs small" style="left:108px;top:30px;width:170px">"Lorem ipsum dolor sit amet, consectetur adipisicing elit, sed do eiusmod tempor incididunt ut labore et dolore magna aliqua. Ut enim ad minim veniam.</p>
  <p class="abs small" style="left:12px;top:110px;width:267px">Lorem ipsum dolor sit amet, consectetur adipisicing elit, sed do eiusmod tempor incididunt ut labore et dolore magna aliqua. Ut enim ad minim veniam, quis nostrud exercitation ullamco laboris nisi ut aliquip ex ea commodo consequat. Lorem ipsum dolor sit amet, consectetur adipisicing elit, sed do eiusmod tempor incididunt ut labore et dolore magna aliqua. Ut enim ad minim veniam, quis nostrud exercitation ullamco laboris nisi ut aliquip ex ea commodo consequat.</p>
  <div class="abs btn-sq" style="left:190px;top:241px">Read more</div>
</section>

<!-- Quick contact -->
<div class="abs tab" style="left:708px"><b>3</b>Quick Contact....</div>
<section class="abs col" style="left:671px"></section>
<form>
  <div class="abs label" style="left:662px;top:813px">Name :</div>
  <div class="abs field" style="top:805px"></div>
  <div class="abs label" style="left:662px;top:856px">Phone :</div>
  <div class="abs field" style="top:848px"></div>
  <div class="abs label" style="left:662px;top:901px">Email Id :</div>
  <div class="abs field" style="top:892px"></div>
  <div class="abs check"></div>
  <div class="abs check-label">Subscribe to our Newsletter</div>
  <div class="abs submit">Submit</div>
</form>

<footer>
  <div class="abs footer-top"></div>
  <div class="abs footer"></div>
  <ul class="abs footer-links" style="left:85px"><li>About Us</li><li>Contact Us</li><li>Services</li><li>lorem ipsum</li><li>other links</li></ul>
  <ul class="abs footer-links" style="left:253px"><li>About Us</li><li>Contact Us</li><li>Services</li><li>lorem ipsum</li><li>other links</li></ul>
  <ul class="abs footer-links" style="left:427px"><li>About Us</li><li>Contact Us</li><li>Services</li><li>lorem ipsum</li><li>other links</li></ul>
  <div class="abs footer-brand">Tavernor Brook Finance</div>
  <div class="abs copyright">Copyright Statement</div>
</footer>

</body>
</html>
```